A new website for Electrical Contractor Business

We are looking for a unique and new WordPress website design which would include 5 Pages - Home Page, Meet the Team, Our Services, Our Projects and Contact Us page.

The global theme for the website needs to be professional but simple to navigate as we cater for both business and home owner customers.

Our core business service is targeted around lighting from single room decorative to large office so the theme should incorporate this in some way.

The home page should include;
Our business logo, Contact number, Email address, small Image rotation box - Highlighting pervious projectsText box - With welcome message, chirpnet feed news reel/Customer feed back box.

I would also like to see a 2 boxes for the separate customer types we services. Business and Home Owner. each box will have a small image with a small text description with a link to the area of the services page relevant to that customer type.

Meet the team page -This will be introducing potential customers to the team so I would like it to include for each team member. Something like a small image and text area which will introduce an outline of the team members skills and abilities.

Our Services page This page will be outlining the different services on offer to the both customer types business and homeowner. Each service should have an image with text description of the service would good here.

Our projects page-Will include images of pervious projects and work we have completed along with a text area for the project description/ outliner.

Contact Us page - Should include a contact form which should include an option for the customer to quest us to call them back, also a selection box for them to inform us our how they found our details would be good.

Colour - The theme colours can be taken from the logo or feel free to impress with your own imagination.

Remember we are looking for a website that will interest our customers enough to except our services or be drawn further into the website.. So call to action links to other areas of the site/ contact page are welcome

Target Market(s)

Business - Office, warehousing and Large Store - lighting and Power
Home owner lighting and power

Coding

Coded - Design and coding required

Number of Pages Required

5+ page

Font styles to use
Serif
Sans Serif

Colors

Designer to choose colors to be used in the design.

Requirements
Must have
• Logo integrated into the website design - i.e. website colours which allow the logo to blend into the design.
Nice to have
• Custom but professional theme catering to business customers, but also show that we do provide services to home owners too.
Should not have
• Sorry am not interested in one oversized block image on rotation covering half the home page.. Images will be needed but not a single block over sized frame with not text, shape. Please use your imagination when considering this design

```html
<!DOCTYPE html>
<html lang="en">
<head>
<meta charset="utf-8">
<title>Brightline Electrical</title>
<link rel="stylesheet" href="https://fonts.googleapis.com/css2?family=Roboto:wght@300;400;500;700&family=Montserrat:wght@400;500;600;700&display=swap">
<style>
:root{
  --navy:#1d2a52;
  --navy-dark:#141d3a;
  --orange:#f26a21;
  --ink:#2a2f3d;
  --muted:#7a8090;
  --soft:#f3f4f8;
  --white:#ffffff;
  --footer:#262a33;
  --footer-dark:#1c1f26;
}
*{box-sizing:border-box;margin:0;padding:0}
html,body{width:1200px;height:3756px;overflow:hidden}
body{font-family:"Roboto",Arial,sans-serif;color:var(--ink);background:var(--white);font-size:13px;line-height:1.6}
.container{width:740px;margin:0 auto;position:relative;height:100%}
.section-title{font-family:"Montserrat",Arial,sans-serif;font-weight:500;font-size:18px;text-align:center;color:var(--navy);text-transform:uppercase;letter-spacing:.5px}
.section-title b{font-weight:700}
.section-title::after{content:"";display:block;width:36px;height:3px;background:var(--orange);margin:8px auto 0}
.btn{display:inline-block;background:var(--orange);color:var(--white);font-size:10px;font-weight:700;text-transform:uppercase;padding:8px 18px;border-radius:2px;letter-spacing:.5px;line-height:1.4}
.btn-light{background:var(--white);color:var(--ink)}
.ph{display:block}

.topbar{height:28px;background:var(--navy-dark);color:#cfd4e3;font-size:10px}
.topbar .container{display:flex;justify-content:space-between;align-items:center}
.topbar span{display:inline-flex;align-items:center;gap:6px}
.topbar .dot{width:7px;height:7px;border-radius:50%;background:var(--orange)}

.header{height:80px;background:var(--white);box-shadow:0 1px 6px rgba(0,0,0,.08);position:relative;z-index:2}
.header .container{display:flex;align-items:center;justify-content:space-between}
.brand{display:flex;align-items:center;gap:8px;font-family:"Montserrat",sans-serif;font-weight:700;font-size:15px;color:var(--navy)}
.brand i{width:26px;height:26px;border-radius:50%;background:var(--orange);display:block}
.nav{display:flex;align-items:center;gap:18px;font-size:9px;font-weight:500;text-transform:uppercase;color:var(--ink)}
.nav .active{color:var(--orange);border-bottom:2px solid var(--orange);padding-bottom:3px}

.hero{height:345px;position:relative;overflow:hidden}
.hero .bg{position:absolute;inset:0;background:linear-gradient(100deg,#2b4f8a 0%,#4d7fbe 45%,#8fb3d9 75%,#5b7ea8 100%)}
.hero-copy{position:absolute;left:0;top:80px;color:var(--white)}
.hero-copy .lead{font-family:"Montserrat",sans-serif;font-size:24px;font-weight:400;line-height:1.2}
.hero-copy h1{font-family:"Montserrat",sans-serif;font-size:36px;font-weight:700;line-height:1.15;margin-bottom:10px}
.hero-copy p{font-size:12px;width:300px;margin-bottom:18px;opacity:.9}

.welcome{height:390px;padding-top:44px}
.welcome-grid{display:flex;justify-content:space-between;margin-top:34px}
.welcome-text{width:330px;font-size:11px;color:var(--muted);line-height:1.55}
.welcome-text strong{color:var(--ink);display:block;margin-bottom:8px}
.ticks{list-style:none;margin-top:8px}
.ticks li{display:flex;align-items:center;gap:8px;margin-bottom:2px}
.ticks svg{flex:none}
.features{display:grid;grid-template-columns:1fr 1fr;gap:26px 22px;width:370px}
.feature{display:flex;gap:10px}
.feature .ic{width:32px;height:32px;border:2px solid var(--orange);border-radius:50%;flex:none;display:flex;align-items:center;justify-content:center}
.feature h4{font-size:11px;color:var(--navy);font-weight:700}
.feature p{font-size:10px;color:var(--muted);line-height:1.5}

.projects{height:720px;background:var(--soft);padding-top:50px}
.filters{display:flex;justify-content:center;gap:10px;margin:28px 0 26px}
.filters span{font-size:10px;padding:6px 14px;border:1px solid #c9ccd6;background:var(--white)}
.filters .on{background:var(--orange);color:var(--white);border-color:var(--orange)}
.grid{display:grid;grid-template-columns:repeat(3,232px);gap:16px;justify-content:center}
.tile{height:232px}
.tile.feature-tile{background:var(--navy);display:flex;flex-direction:column;align-items:center;justify-content:center;color:var(--white);font-size:11px;text-transform:uppercase;gap:10px}
.t1{background:linear-gradient(135deg,#c9b49a,#7d6a58)}
.t2{background:linear-gradient(135deg,#e8e2d8,#9aa0a6)}
.t3{background:linear-gradient(135deg,#e59a4a,#3f4a5c)}
.t4{background:linear-gradient(135deg,#d7d2c6,#6c7484)}
.t5{background:linear-gradient(135deg,#3b6fb0,#b6c94a)}

.services{height:560px;padding-top:50px}
.service-row{display:flex;justify-content:center;gap:16px;margin-top:30px}
.service-card{width:360px;height:408px;color:var(--white);text-align:center}
.service-card .ph{height:190px}
.service-card.orange{background:var(--orange)}
.service-card.navy{background:var(--navy)}
.service-card .badge{width:46px;height:46px;border-radius:50%;background:var(--white);margin:-23px auto 14px;display:flex;align-items:center;justify-content:center}
.service-card h3{font-family:"Montserrat",sans-serif;font-size:15px;font-weight:700;margin-bottom:6px}
.service-card p{font-size:11px;padding:0 50px;margin-bottom:18px;opacity:.9}

.testimonials{height:400px;background:linear-gradient(180deg,#f7f8fb,#eef0f5);text-align:center;padding-top:80px}
.testimonials h2{font-family:"Montserrat",sans-serif;font-size:22px;font-weight:600;color:var(--navy);margin-bottom:12px}
.testimonials p{width:520px;margin:0 auto 12px;font-size:11px;color:var(--muted)}
.who{font-size:10px;font-weight:700;color:var(--ink)}
.who .stars{color:var(--orange);letter-spacing:2px;margin-left:6px}
.avatars{display:flex;justify-content:center;gap:10px;margin-top:28px}
.avatars i{width:34px;height:34px;border-radius:50%;background:#b9bfcc;display:block}
.avatars i.on{background:#8a93a6;box-shadow:0 0 0 3px var(--white),0 0 0 4px var(--orange)}

.news{height:460px;padding-top:50px}
.news-row{display:flex;justify-content:center;gap:16px;margin-top:30px}
.news-card{width:232px;background:var(--white);box-shadow:0 2px 10px rgba(0,0,0,.08)}
.news-card .ph{height:140px}
.n1{background:linear-gradient(135deg,#d8a070,#6d5d55)}
.n2{background:linear-gradient(135deg,#e09550,#5d6b80)}
.n3{background:linear-gradient(135deg,#e7e0d3,#98836e)}
.news-card h4{font-size:11px;font-weight:700;color:var(--navy);padding:12px 14px 4px;line-height:1.4}
.news-card p{font-size:10px;color:var(--muted);padding:0 14px 14px}

.quote{height:528px;background:linear-gradient(100deg,var(--navy-dark) 0%,var(--navy) 60%,#2d4474 100%);color:var(--white);padding-top:50px}
.quote .section-title{color:var(--white)}
.quote .intro{width:560px;margin:16px auto 34px;text-align:center;font-size:10px;opacity:.8}
.quote-body{display:flex;align-items:flex-start}
.call{width:300px;text-align:center;padding-top:40px;border-right:1px solid rgba(255,255,255,.2);height:250px}
.call .ring{width:40px;height:40px;border-radius:50%;background:var(--orange);margin:0 auto 12px;display:flex;align-items:center;justify-content:center}
.call .label{font-size:13px}
.call .number{font-family:"Montserrat",sans-serif;font-size:28px;font-weight:700;line-height:1.3}
.call .small{font-size:12px;opacity:.9}
.form{width:400px;margin-left:40px;display:grid;grid-template-columns:1fr 1fr;gap:10px}
.field{height:30px;background:rgba(255,255,255,.96);font-size:9px;color:#9096a4;padding:8px 10px}
.field.area{grid-column:1/3;height:80px}
.form .btn{grid-column:1/3;justify-self:center;margin-top:8px}

.footer{height:245px;background:var(--footer);color:#b9bdc7}
.footer-main{height:205px;padding-top:44px}
.footer-cols{display:flex;justify-content:space-between}
.footer .brand{color:var(--white);font-size:15px}
.footer-about{width:200px}
.footer-about p{font-size:10px;margin-top:12px}
.col h5,.mail h5{color:var(--white);font-size:11px;font-weight:700;margin-bottom:10px}
.col li{list-style:none;font-size:10px;margin-bottom:6px}
.mail{width:220px}
.mail .signup{display:flex;margin-bottom:10px}
.mail .signup div{flex:1;height:28px;background:var(--white);font-size:9px;color:#9096a4;padding:7px 10px}
.mail .signup span{width:32px;height:28px;background:var(--orange);display:flex;align-items:center;justify-content:center}
.mail p{font-size:10px}
.social{display:flex;gap:8px;margin-top:12px}
.social i{width:18px;height:18px;border-radius:50%;background:#454a56;display:block}
.copyright{height:40px;background:var(--footer-dark);font-size:10px}
.copyright .container{display:flex;align-items:center}
</style>
</head>
<body>

<div class="topbar">
  <div class="container">
    <span><i class="dot"></i>+91 90000 12345</span>
    <span><i class="dot"></i>info@brightlineelectric.com</span>
  </div>
</div>

<header class="header">
  <div class="container">
    <div class="brand"><i></i>Brightline Electrical</div>
    <nav class="nav">
      <span class="active">Home</span>
      <span>Meet the Team</span>
      <span>Our Services</span>
      <span>Projects</span>
      <span>Contact Us</span>
      <span class="btn">Get a Quote</span>
    </nav>
  </div>
</header>

<section class="hero">
  <div class="bg" role="img" aria-label="Night city skyline with glowing lights and an electrician in a hard hat and safety vest on the right"></div>
  <div class="container">
    <div class="hero-copy">
      <div class="lead">Fast &amp; Reliable</div>
      <h1>Electrical Services</h1>
      <p>Lighting and power for homes, offices, warehouses and large stores.</p>
      <span class="btn">Get a Quote</span>
    </div>
  </div>
</section>

<section class="welcome">
  <div class="container">
    <h2 class="section-title">Welcome to <b>Brightline Electrical</b></h2>
    <div class="welcome-grid">
      <div class="welcome-text">
        <strong>Trusted electrical contractors for lighting and power, from a single decorative room to a full office floor.</strong>
        <p>We plan, install and maintain safe, efficient systems for business and home owners with clear pricing and tidy work.</p>
        <ul class="ticks">
          <li><svg width="11" height="11" viewBox="0 0 12 12"><path d="M2 6l3 3 5-6" fill="none" stroke="#f26a21" stroke-width="2"/></svg>Certified and insured electricians</li>
          <li><svg width="11" height="11" viewBox="0 0 12 12"><path d="M2 6l3 3 5-6" fill="none" stroke="#f26a21" stroke-width="2"/></svg>Office and warehouse lighting design</li>
          <li><svg width="11" height="11" viewBox="0 0 12 12"><path d="M2 6l3 3 5-6" fill="none" stroke="#f26a21" stroke-width="2"/></svg>Home rewiring and upgrades</li>
          <li><svg width="11" height="11" viewBox="0 0 12 12"><path d="M2 6l3 3 5-6" fill="none" stroke="#f26a21" stroke-width="2"/></svg>24/7 emergency call-outs</li>
          <li><svg width="11" height="11" viewBox="0 0 12 12"><path d="M2 6l3 3 5-6" fill="none" stroke="#f26a21" stroke-width="2"/></svg>Free on-site quotes</li>
        </ul>
      </div>
      <div class="features">
        <div class="feature"><div class="ic"><svg width="14" height="14" viewBox="0 0 16 16"><path d="M9 1L3 9h4l-1 6 6-8H8z" fill="#f26a21"/></svg></div><div><h4>Industrial Services</h4><p>Power and lighting for large sites, built to last.</p></div></div>
        <div class="feature"><div class="ic"><svg width="14" height="14" viewBox="0 0 16 16"><path d="M2 8l6-5 6 5v6H2z" fill="none" stroke="#f26a21" stroke-width="1.6"/></svg></div><div><h4>Residential Services</h4><p>Safe wiring and lighting for every room at home.</p></div></div>
        <div class="feature"><div class="ic"><svg width="14" height="14" viewBox="0 0 16 16"><circle cx="8" cy="7" r="4" fill="none" stroke="#f26a21" stroke-width="1.6"/><path d="M6 13h4" stroke="#f26a21" stroke-width="1.6"/></svg></div><div><h4>Detailed Service</h4><p>Careful planning and neat, tested installations.</p></div></div>
        <div class="feature"><div class="ic"><svg width="14" height="14" viewBox="0 0 16 16"><path d="M3 3c0 6 4 10 10 10l1-3-3-1-1 1c-2-1-3-2-4-4l1-1-1-3z" fill="#f26a21"/></svg></div><div><h4>Quick Support</h4><p>Fast response when you need help the most.</p></div></div>
      </div>
    </div>
  </div>
</section>

<section class="projects">
  <div class="container">
    <h2 class="section-title">Our <b>Latest Projects</b></h2>
    <div class="filters">
      <span class="on">All Projects</span><span>Residential Services</span><span>Commercial Services</span><span>Industrial Services</span>
    </div>
    <div class="grid">
      <div class="tile feature-tile"><svg width="28" height="28" viewBox="0 0 30 30"><path d="M15 3v24M3 15h24" stroke="#fff" stroke-width="2"/></svg>Residential Lighting</div>
      <div class="tile ph t1" role="img" aria-label="Electrician working on a ceiling light"></div>
      <div class="tile ph t2" role="img" aria-label="Technician checking a wall outlet"></div>
      <div class="tile ph t3" role="img" aria-label="Electrician installing cables at height"></div>
      <div class="tile ph t4" role="img" aria-label="Electrician fitting a wall fixture"></div>
      <div class="tile ph t5" role="img" aria-label="Electrician in safety vest at a power site"></div>
    </div>
  </div>
</section>

<section class="services">
  <div class="container">
    <h2 class="section-title">Our <b>Services</b></h2>
    <div class="service-row">
      <div class="service-card orange">
        <div class="ph" role="img" aria-label="Worker in safety gear at an industrial site at dusk" style="background:linear-gradient(135deg,#e08a3c,#3b4560)"></div>
        <div class="badge"><svg width="20" height="20" viewBox="0 0 22 22"><path d="M2 20V10l5 3V10l5 3V6h8v14z" fill="#f26a21"/></svg></div>
        <h3>Industrial Services</h3>
        <p>Lighting and power for offices, warehouses and large stores.</p>
        <span class="btn btn-light">Read More</span>
      </div>
      <div class="service-card navy">
        <div class="ph" role="img" aria-label="Electrician fixing wiring inside a home" style="background:linear-gradient(135deg,#e7e1d6,#8a8f9c)"></div>
        <div class="badge"><svg width="20" height="20" viewBox="0 0 22 22"><path d="M2 11l9-8 9 8M5 9v10h12V9" fill="none" stroke="#1d2a52" stroke-width="2"/></svg></div>
        <h3>Residential Services</h3>
        <p>Decorative lighting, rewiring and power for home owners.</p>
        <span class="btn btn-light">Read More</span>
      </div>
    </div>
  </div>
</section>

<section class="testimonials">
  <div class="container">
    <h2>What People are Saying...</h2>
    <p>The team rewired our office and upgraded all the lighting in two days. They were tidy, on time and explained every step clearly. We would happily hire them again.</p>
    <div class="who">— Laura Bennett <span class="stars">★★★★★</span></div>
    <div class="avatars"><i></i><i class="on"></i><i></i></div>
  </div>
</section>

<section class="news">
  <div class="container">
    <h2 class="section-title">Latest <b>News</b></h2>
    <div class="news-row">
      <div class="news-card"><div class="ph n1" role="img" aria-label="Electrician fitting a light fixture"></div><h4>Five ways to cut lighting costs in your office</h4><p>Simple upgrades that lower bills fast.</p></div>
      <div class="news-card"><div class="ph n2" role="img" aria-label="Electrician working in a warehouse"></div><h4>Warehouse LED refit completed this month</h4><p>Brighter aisles and lower energy use.</p></div>
      <div class="news-card"><div class="ph n3" role="img" aria-label="Electrician testing a home switchboard"></div><h4>When should you rewire an older home?</h4><p>Signs your wiring needs attention.</p></div>
    </div>
  </div>
</section>

<section class="quote">
  <div class="container">
    <h2 class="section-title">Let's Get You <b>Free Quote</b></h2>
    <p class="intro">Tell us about your project and we will call you back with a clear, free quote. Business or home, large or small, our team is ready to help with lighting and power.</p>
    <div class="quote-body">
      <div class="call">
        <div class="ring"><svg width="20" height="20" viewBox="0 0 22 22"><path d="M4 3c0 9 6 15 15 15l1-4-4-1-2 2c-3-1-5-3-6-6l2-2-1-4z" fill="#fff"/></svg></div>
        <div class="label">Call our Friendly Team</div>
        <div class="number">+91 90000 12345</div>
        <div class="small">24/7 Emergency Service</div>
      </div>
      <div class="form">
        <div class="field">Full Name</div>
        <div class="field">Email</div>
        <div class="field">Phone</div>
        <div class="field">Service</div>
        <div class="field area">Your Requirements</div>
        <span class="btn">Get a Free Quote</span>
      </div>
    </div>
  </div>
</section>

<footer class="footer">
  <div class="footer-main">
    <div class="container">
      <div class="footer-cols">
        <div class="footer-about">
          <div class="brand"><i></i>Brightline Electrical</div>
          <p>Lighting and power specialists for business and home owners.</p>
        </div>
        <div class="col"><h5>Useful Links</h5><ul><li>Home</li><li>Services</li><li>Our Projects</li></ul></div>
        <div class="col"><h5>Company</h5><ul><li>Meet the Team</li><li>About Us</li><li>Contact</li></ul></div>
        <div class="mail">
          <h5>Join Our Mailbox</h5>
          <div class="signup"><div>Your email address</div><span><svg width="12" height="12" viewBox="0 0 14 14"><path d="M1 7h11M8 3l4 4-4 4" stroke="#fff" stroke-width="2" fill="none"/></svg></span></div>
          <p>Subscribe for lighting tips and news.</p>
          <div class="social"><i></i><i></i><i></i><i></i></div>
        </div>
      </div>
    </div>
  </div>
  <div class="copyright"><div class="container">Copyright © 2024 Brightline Electrical | Privacy Policy</div></div>
</footer>

</body>
</html>
```